Glossaro: Graphic elements & webpage layout

Hi there! We’re building a site called Glossaro.com—it will be a community site for beauty product reviews, product recommendations and beauty tutorials. We've already got a logo, thanks to another ArtHively project. This project on ArtHively involves the following web design work:

1) Propose the overall graphic design elements of our site (according to our guidelines, which are in the attached file)

-Color Palette
-Fonts
-Icon set(s)

2) Using the overall graphic design elements in step 1 and our storyboard (attached), develop a webpage layout for the "How-to" page of our site. The "How-to" pages will be an editorial format, where our beauty journalist will show a video (and photos) of step-by-step beauty tutorials.

Please take a look at the attached files for a detailed brief and the logo! Thanks and we're looking forward to working with you!

Target Market(s)

Glossaro is for a French, English, and American audience of women between the ages of 16 and 30, who buy and use beauty products regularly.

Industry/Entity Type

Graphic Design

Requirements
Must have
• 1) A global set of graphic standards for the website Glossaro.com:
• A color palette
• Fonts
• An icon set (or sets)
• A menu
• Other graphic elements like button styles

2) A webpage layout (non-coded) for the How-To page template
(See storyboard, attached separately)
This webpage layout is for the main editorial format on Glossaro—step by step beauty tutorials. The individual on-page elements are in the storyboard, but overall we’d like it to look clean, friendly, and to encourage community participation and sharing on social networks.
Nice to have
• • A look and feel that is fresh, clean and modern
• Proximity: Establishes a close proximity with the user. (We want them to get the same feeling they get when talking beauty tips with their close friends).
• Neutrality: A sincere and neutral look and feel that doesn’t suggest a preference for any particular or elite type of beauty (but it can still be fun!)
• The graphic design is relevant to the beauty sector as a whole. (We could be talking about lipstick, a hairbrush or a man’s cologne)
• The graphic design alludes to the beauty industry (discreetly, not overtly!)
Should not have
• We've already got a logo, so you shouldn't suggest a new one!

We really want to avoid designs that are too traditionally "beauty" or too girly and feminine. Please no pink, no flowers, etc! :)

```html
<!DOCTYPE html>
<html lang="fr">
<head>
<meta charset="utf-8">
<title>Glossaro – titre du tutorial</title>
<link href="https://fonts.googleapis.com/css2?family=Arimo:ital,wght@0,400;0,700;1,400&family=Rokkitt:wght@300;400;700&display=swap" rel="stylesheet">
<style>
  :root {
    --orange: #ff9a2e;
    --orange-dark: #e07a12;
    --teal-light: #0cc4b0;
    --teal: #1fb3a2;
    --teal-dark: #1a8e80;
    --mint-bg: #c9f1ea;
    --mint-soft: #d3f4ee;
    --ink: #222222;
    --text-grey: #555555;
    --white: #ffffff;
    --border: #2f3a38;
  }
  * { box-sizing: border-box; margin: 0; padding: 0; }
  html, body { width: 1200px; height: 900px; overflow: hidden; }
  body {
    position: relative;
    background: var(--mint-bg);
    font-family: "Arimo", Arial, sans-serif;
    color: var(--ink);
  }
  .top-bar {
    position: absolute; left: 0; top: 0; width: 1200px; height: 25px;
    background: var(--orange);
  }
  .top-bar a {
    position: absolute; top: 5px; font-size: 12px; color: var(--white); text-decoration: none;
  }
  .page {
    position: absolute; left: 134px; top: 67px; width: 951px; height: 860px;
    background: var(--white); border: 1px solid var(--border); border-radius: 8px;
    overflow: hidden;
  }
  .page > * { position: absolute; }
  .brand {
    left: 12px; top: 10px; display: flex; align-items: center; gap: 12px;
    font-family: "Rokkitt", Georgia, serif; font-weight: 700; font-size: 72px; color: var(--ink);
    line-height: 1;
  }
  .brand-dot { width: 22px; height: 22px; border-radius: 50%; background: var(--teal); }
  .main-nav {
    left: 332px; top: 36px; width: 619px; height: 52px;
    background: linear-gradient(var(--teal-light), var(--teal-dark));
    border-top: 1px solid #0a9c8c; box-shadow: 0 2px 3px rgba(0,0,0,.25);
  }
  .main-nav a {
    position: absolute; top: 0; height: 52px; line-height: 52px; text-align: center;
    color: var(--white); font-weight: 700; font-size: 16px; text-decoration: none;
    border-right: 1px solid rgba(255,255,255,.3);
  }
  .nav-howto { left: 0; width: 125px; }
  .nav-tips { left: 125px; width: 123px; }
  .search {
    position: absolute; left: 318px; top: 15px; width: 278px; height: 23px;
    background: var(--white); border: 2px solid #6b6b6b; border-radius: 12px;
    font-style: italic; font-size: 13px; color: #bbbbbb; padding: 2px 0 0 28px;
  }
  .search svg { position: absolute; left: 6px; top: 3px; }
  .tutorial-title {
    left: 11px; top: 150px; font-family: "Rokkitt", Georgia, serif; font-weight: 400;
    font-size: 44px; color: var(--ink);
  }
  .social-btn {
    top: 158px; height: 36px; background: var(--mint-soft); border-radius: 3px;
    color: var(--teal); font-size: 14px; display: flex; align-items: center; gap: 6px; padding: 0 8px;
  }
  .social-btn .sq { width: 20px; height: 20px; background: var(--teal); border-radius: 3px; }
  .share { left: 310px; width: 107px; }
  .like { left: 436px; width: 68px; }
  .video-meta {
    left: 10px; top: 210px; width: 500px; height: 30px;
    background: linear-gradient(var(--teal-light), var(--teal-dark));
    border: 1px solid var(--border); border-bottom: 0; border-radius: 6px 6px 0 0;
    color: var(--white); font-size: 14px;
  }
  .video-meta span { position: absolute; top: 6px; }
  .difficulty-dot { position: absolute; top: 8px; width: 16px; height: 13px; border-radius: 50%; background: var(--orange); }
  .difficulty-dot.half { background: linear-gradient(var(--orange) 50%, var(--white) 50%); }
  .video {
    left: 10px; width: 500px; background: linear-gradient(#6a6a6a, #000000);
  }
  .video-main { top: 239px; height: 301px; }
  .video-main svg { position: absolute; left: 230px; top: 124px; }
  .intro {
    left: 11px; top: 557px; width: 490px; font-size: 13.4px; line-height: 17px; color: var(--text-grey);
  }
  .step-title { left: 10px; top: 653px; font-family: "Rokkitt", Georgia, serif; font-size: 24px; }
  .tab {
    top: 706px; width: 74px; height: 31px; border: 1px solid var(--border); border-bottom: 0;
    border-radius: 6px 6px 0 0; color: var(--white); font-weight: 700; font-size: 14px;
    text-align: center; line-height: 28px;
  }
  .tab-video { left: 10px; background: linear-gradient(var(--orange), var(--orange-dark)); }
  .tab-photos { left: 91px; background: linear-gradient(var(--teal-light), var(--teal-dark)); }
  .video-step { top: 736px; height: 130px; border-top: 1px solid var(--border); }
  .divider { left: 538px; top: 182px; height: 700px; border-left: 1px dashed #999; }
  .sidebar-title { left: 567px; top: 163px; font-family: "Rokkitt", Georgia, serif; font-size: 24px; }
  .products-box {
    left: 576px; top: 210px; width: 374px; height: 331px;
    background: linear-gradient(#00c6b4, #1e8878); box-shadow: 0 3px 6px rgba(0,0,0,.35);
    padding: 29px 0 0 28px; color: var(--white); font-size: 14px; line-height: 17px; list-style: none;
  }
  .product-card {
    left: 567px; top: 737px; width: 353px; height: 100px; background: var(--mint-soft);
  }
  .product-thumb { position: absolute; left: 0; top: 0; width: 92px; height: 100px; background: #2db9a9; }
  .product-info {
    position: absolute; left: 106px; top: 3px; font-size: 14px; line-height: 17px; color: var(--text-grey);
  }
  .buy-btn {
    position: absolute; left: 104px; top: 60px; width: 92px; height: 29px;
  }
  .buy-btn span {
    position: absolute; left: 10px; top: 5px; color: var(--white); font-weight: 700; font-size: 16px;
  }
</style>
</head>
<body>
  <header class="top-bar">
    <a style="left:805px">Choix de la langue</a>
    <a style="left:937px">Chirpline</a>
    <a style="left:1001px">Circlebook</a>
  </header>

  <main class="page">
    <div class="brand">Glossaro<span class="brand-dot"></span></div>

    <nav class="main-nav">
      <a class="nav-howto">How to</a>
      <a class="nav-tips">Tips</a>
      <div class="search">
        <svg width="16" height="16" viewBox="0 0 16 16"><circle cx="6.5" cy="6.5" r="4.5" fill="none" stroke="#bbb" stroke-width="2"/><line x1="10" y1="10" x2="14" y2="14" stroke="#bbb" stroke-width="2.5" stroke-linecap="round"/></svg>
        Search...
      </div>
    </nav>

    <h1 class="tutorial-title">titre du tutorial</h1>
    <div class="social-btn share">Share <span class="sq"></span><span class="sq"></span></div>
    <div class="social-btn like">Like <span class="sq"></span></div>

    <div class="video-meta">
      <span style="left:17px">Difficulté:</span>
      <i class="difficulty-dot" style="left:78px"></i>
      <i class="difficulty-dot" style="left:106px"></i>
      <i class="difficulty-dot half" style="left:136px"></i>
      <span style="left:188px">Durée: 20 minutes</span>
      <span style="left:366px">Occasion: Soirée</span>
    </div>
    <div class="video video-main" role="img" aria-label="Lecteur vidéo du tutoriel">
      <svg width="44" height="54" viewBox="0 0 44 54"><polygon points="0,0 44,27 0,54" fill="#1fb3a2"/></svg>
    </div>

    <p class="intro">Lorem ipsum dolor sit amet, maiores ornare ac fermentum, imperdiet ut vivamus a, nam lectus at nunc. Quam euismod sem, semper ut potenti pellentesque quisque. In eget sapien sed, sit duis vestibulum ultricies, placerat morbi amet vel, nullam in in lorem vel.</p>

    <h2 class="step-title">etape 1</h2>
    <div class="tab tab-video">Vidéo</div>
    <div class="tab tab-photos">Photos</div>
    <div class="video video-step" role="img" aria-label="Vidéo de l'étape 1"></div>

    <div class="divider"></div>

    <h2 class="sidebar-title">Les produits nécessaires</h2>
    <ul class="products-box">
      <li>Produit 1</li>
      <li>Produit 2</li>
      <li>Produit 3</li>
      <li>...</li>
    </ul>

    <div class="product-card">
      <div class="product-thumb" role="img" aria-label="Photo du produit 1"></div>
      <div class="product-info">Produit 1<br>Lorem ipsum dolor sit amet, maiores<br>Prix</div>
      <div class="buy-btn">
        <svg width="92" height="29" viewBox="0 0 92 29"><defs><linearGradient id="buyGrad" x1="0" y1="0" x2="0" y2="1"><stop offset="0" stop-color="#0cc4b0"/><stop offset="1" stop-color="#1a8e80"/></linearGradient></defs><path d="M4 .5 H76 L91 14.5 L76 28.5 H4 Q.5 28.5 .5 25 V4 Q.5 .5 4 .5Z" fill="url(#buyGrad)" stroke="#2f3a38"/></svg>
        <span>Acheter</span>
      </div>
    </div>
  </main>
</body>
</html>
```